Naturopath specialising in Children's Health

I have just started working in a new clinic where I will be predominantly treating children so I would like to rebrand with a business card that reflects this.

I would like a clever design which is subtly playful and will attract children and parents alike, while maintaining a professional look. It must also reflect that I utilize natural medicine - including herbal medicine and nutrition as part of my treatment. Employing the use of a plant or herb would be ideal. I had envisioned the image of a dandelion blowing in the wind (or being blown by a child) as a great combination of the playful yet natural medicine I am trying to ecompass in the card.

I would like to use yellow, orange, blue or green as the dominant colour for the card.

The front of the card should contain the logo and the words 'Maribel Stroud - Naturopath.'

The back of the card should contain the following details:
Maribel Stroud BHSc Nat, Dip RM
Naturopath, Herbalist, Nutritionist, Iridologist, Remedial Massage Therapist, Reiki Practitioner
0417 382 961
Thistle Kenwick - (02) 9463 1508
maribel.stroud@fernmail.example
HWPA 47183

```html
<!DOCTYPE html>
<html lang="en">
<head>
<meta charset="utf-8">
<title>Maribel Stroud - Naturopath · Business Card</title>
<link rel="stylesheet" href="https://fonts.googleapis.com/css2?family=PT+Sans:wght@400;700&display=swap">
<style>
  :root {
    --backdrop: #8b5e3c;
    --teal: #2fc0bd;
    --white: #ffffff;
    --swoosh-grey: #77797b;
    --ink: #1c1c1c;
    --divider: #1f5f5d;
    --bullet: #9a9a9a;
    --seed-light: #f4f7e6;
    --seed-mid: #d8e9a8;
  }
  * { box-sizing: border-box; margin: 0; padding: 0; }
  html, body {
    width: 1200px; height: 480px; overflow: hidden;
    background: var(--backdrop);
    font-family: "PT Sans", Arial, sans-serif;
  }
  .canvas { position: relative; width: 1200px; height: 480px; }

  .card {
    position: absolute; top: 94px;
    width: 484px; height: 272px;
    border-radius: 14px; overflow: hidden;
  }
  .card--front { left: 58px; background: var(--white); }
  .card--back { left: 596px; background: var(--teal); }

  .card__wave { position: absolute; inset: 0; width: 100%; height: 100%; }

  .dandelion-art {
    position: absolute; left: 30px; top: 112px;
    width: 58px; height: 58px; border-radius: 50%;
    background: radial-gradient(circle at 50% 50%, var(--seed-light) 0%, var(--seed-mid) 70%, rgba(216,233,168,0) 100%);
  }

  .card__title {
    position: absolute; left: 0; right: 0; top: 72px;
    text-align: center; font-weight: 700; font-size: 32px;
    line-height: 1;
  }
  .card--front .card__title { color: var(--teal); }
  .card--back .card__title { top: 70px; color: var(--white); text-shadow: 1px 2px 2px rgba(0,0,0,0.45); }

  .card__credentials {
    position: absolute; left: 0; right: 0; top: 112px;
    text-align: center; font-size: 13px; color: var(--white); line-height: 1;
  }

  .card__clinic { font-size: 17px; color: var(--ink); line-height: 1; }
  .card--front .card__clinic {
    position: absolute; left: 0; right: 0; top: 166px;
    text-align: center; padding-left: 18px;
  }

  .services { position: absolute; left: 52px; top: 145px; list-style: none; }
  .services li {
    position: relative; padding-left: 12px;
    font-size: 12.5px; font-weight: 700; color: var(--white);
    line-height: 17.8px;
  }
  .services li::before {
    content: ""; position: absolute; left: 0; top: 4.5px;
    width: 8px; height: 8px; border-radius: 50%;
    background: radial-gradient(circle at 35% 35%, #e6e6e6, var(--bullet));
  }

  .divider {
    position: absolute; left: 241px; top: 146px;
    width: 1px; height: 102px; background: var(--divider);
  }

  .contact { position: absolute; left: 252px; top: 174px; }
  .contact .card__clinic { margin-bottom: 7px; }
  .contact__line { font-size: 12px; line-height: 18px; color: var(--ink); }
  .contact__label { font-weight: 700; color: var(--white); }
</style>
</head>
<body>
<main class="canvas">

  <section class="card card--front" aria-label="Card front">
    <svg class="card__wave" viewBox="0 0 484 272" preserveAspectRatio="none" aria-hidden="true">
      <path d="M112 201 C 230 215, 360 195, 484 166 L 484 207 C 380 232, 230 232, 112 201 Z" fill="var(--swoosh-grey)"/>
      <path d="M0 184 C 90 222, 180 238, 280 234 C 360 231, 430 224, 484 218 L 484 272 L 0 272 Z" fill="var(--teal)"/>
    </svg>
    <div class="dandelion-art" role="img" aria-label="Dandelion seed head blowing in the wind"></div>
    <h1 class="card__title">Maribel Stroud - Naturopath</h1>
    <p class="card__clinic">Thistle Kenwick</p>
  </section>

  <section class="card card--back" aria-label="Card back">
    <h2 class="card__title">Maribel Stroud - Naturopath</h2>
    <p class="card__credentials">BHSc Nat, Dip RM</p>
    <ul class="services">
      <li>Naturopath</li>
      <li>Herbalist</li>
      <li>Nutritionist</li>
      <li>Iridologist</li>
      <li>Remedial Massage Therapist</li>
      <li>Reiki Practitioner</li>
    </ul>
    <div class="divider"></div>
    <div class="contact">
      <p class="card__clinic">Thistle Kenwick</p>
      <p class="contact__line"><span class="contact__label">Tel:</span> (02) 9463 1508, 0417 382 961</p>
      <p class="contact__line"><span class="contact__label">Email:</span> maribel.stroud@fernmail.example</p>
      <p class="contact__line">HWPA 47183</p>
    </div>
  </section>

</main>
</body>
</html>
```